KVL Accounting Firm Needs Graphic Art for Our Proven Processes and For Our Core Values

**Looking for redesign of attached Powerpoint content (see below)
***Final graphic should be good for web use

Date: March 10, 2017

From: Dalton Esterby, CPA
Esterby, Lundqvist & Associates, P.C. (KVL)

Background:

KVL is a 20 person Houston based CPA firm, providing tax, accounting, financial and consulting services, to individuals and to entrepreneurs and their businesses. KVL is engaged in a process called QPT (See the book Bedrock, by Alden Forsberg) whereby we implement a “system” to operate our company. As part of this system we have defined what we call our “Proven Process”. This is something we will show all prospective clients, and have on our website, that explains what it looks like to work with us. Starting at the beginning of the project to completion.

Project Description:

KVL is looking for graphic artist assistance in designing the following pieces:

1. Graphic depiction of “The KVL Way”, otherwise known as our “Proven Process”. The first attachments labeled KVL will show what we have done ourselves. These will show the general steps we have defined in both a sort of graphic way and a step by step narrative. The second attachment shows you some actual examples other firms have put together, hopefully that will show you what we are asking you to develop for us. Note that we are very open to any suggested clarifications or improvements to what we have done which may include changing phrases or saying something in a different way. Remember we are accountants!

2. We have defined our core values as a company, and we are wanting to develop some posters/placards so we can post them in our conference rooms, break room, etc. Attached are our core values as well as some deeper narratives about what they mean. Also included are many of the “words” we kicked around before arriving at our core values.

3. You will also find an attachment with our logo that should be incorporated, as well. Designs SHOULD INCLUDE, but not be limited to, the colors on our logo. Our end product should reflect a strong sense of our core values.

We would like to have the project in a form that would give us the option to use any/all of the information on our website, posters, brochures, etc.

Thanks in advance for your assistance.
Updates

Project Deadline Extended Reason: We are in the midst of tax deadlines so need a little more time to review and respond. Added Monday, March 20, 2017

Target Market(s)

Entrepreneurs and their companies with revenue greater than one million; Industries such as real estate, construction, trades and professional services; all in the Greater Houston Texas area

Industry/Entity Type

Accounting

Font styles to use
Serif
Other font styles liked:
• We are okay with Serif but are open.

Requirements
Must have
• Proven Process must be presented in a way that is clear and makes sense.
Nice to have
• Clean lines
• Colors should go with logo (see attached)
Should not have
• Can't think of anything - unless I see it

```html
<!DOCTYPE html>
<html lang="en">
<head>
<meta charset="utf-8">
<title>Client Service Approach – KVL</title>
<link rel="stylesheet" href="https://fonts.googleapis.com/css2?family=Open+Sans:wght@400;600;800&display=swap">
<style>
  :root {
    --olive: #67693a;
    --gold: #bf9a33;
    --ring-2: #9a6c35;
    --ring-3: #7e5532;
    --core: #674431;
    --white: #ffffff;
    --ink: #4b4b3a;
    --page: #ffffff;
  }
  * { margin: 0; padding: 0; box-sizing: border-box; }
  html, body { width: 1200px; height: 927px; overflow: hidden; background: var(--page); }
  .slide {
    position: relative;
    width: 1200px;
    height: 927px;
    font-family: "Open Sans", Arial, sans-serif;
    background: var(--page);
  }
  .slide-title {
    position: absolute;
    left: 72px;
    top: 64px;
    font-size: 50px;
    font-weight: 800;
    letter-spacing: 0.5px;
    color: var(--olive);
    line-height: 1;
  }
  .approach-diagram {
    position: absolute;
    left: 0;
    top: 0;
    width: 1200px;
    height: 927px;
  }
  .ring-label {
    font-family: "Open Sans", Arial, sans-serif;
    font-size: 21px;
    font-weight: 600;
    fill: var(--white);
    text-anchor: middle;
  }
  .firm-sign {
    position: absolute;
    right: 72px;
    top: 748px;
    width: 390px;
    text-align: center;
    color: var(--ink);
  }
  .firm-sign__square {
    display: block;
    width: 44px;
    height: 44px;
    margin: 0 auto 10px;
    background: var(--gold);
  }
  .firm-sign__name,
  .firm-sign__tag {
    font-size: 18px;
    font-weight: 400;
    line-height: 1.35;
    color: var(--ink);
  }
  .firm-sign__name {
    padding-bottom: 6px;
    border-bottom: 1px solid var(--olive);
  }
  .firm-sign__tag {
    padding-top: 4px;
    font-size: 14px;
    letter-spacing: 6px;
  }
  .footer-band {
    position: absolute;
    left: 0;
    bottom: 0;
    width: 1200px;
    height: 18px;
    background: linear-gradient(90deg, var(--gold), var(--olive));
  }
</style>
</head>
<body>
<main class="slide">
  <h1 class="slide-title">CLIENT SERVICE APPROACH</h1>

  <svg class="approach-diagram" viewBox="0 0 1200 927" aria-label="Nested circles: peace of mind, client focus, caring touch, long term relationships">
    <circle cx="600" cy="462" r="280" fill="var(--gold)"/>
    <circle cx="600" cy="518" r="226" fill="var(--ring-2)" stroke="var(--white)" stroke-width="3"/>
    <circle cx="600" cy="575" r="170" fill="var(--ring-3)" stroke="var(--white)" stroke-width="3"/>
    <circle cx="600" cy="631" r="114" fill="var(--core)" stroke="var(--white)" stroke-width="3"/>
    <text class="ring-label" x="600" y="250">Peace of mind</text>
    <text class="ring-label" x="600" y="364">Client focus</text>
    <text class="ring-label" x="600" y="477">Caring touch</text>
    <text class="ring-label" x="600" y="625">Long term</text>
    <text class="ring-label" x="600" y="652">relationships</text>
  </svg>

  <div class="firm-sign">
    <span class="firm-sign__square"></span>
    <p class="firm-sign__name">Esterby, Lundqvist &amp; Associates, PC</p>
    <p class="firm-sign__tag">CPAs &amp; Advisors</p>
  </div>

  <div class="footer-band"></div>
</main>
</body>
</html>
```